KVR Noblesville Sign

I need to have a sign designed for a new self-storage facility we are going to be opening. The sign will be 4'W X 8'H.

Industry/Entity Type

Self Storage

Requirements
Must have
• Harbor Locker Yard logo at the top of the sign, under the logo I want the rendering.
• I also must have this information on the sign:
• 1. OPENING FALL 2016
• 2. Your premier self-storage facility.
• 3. www.harborlockeryard.example

```html
<!DOCTYPE html>
<html lang="en">
<head>
<meta charset="utf-8">
<title>Harbor Locker Yard – Opening Sign</title>
<link rel="stylesheet" href="https://fonts.googleapis.com/css2?family=Open+Sans:wght@300;400;700&family=Oswald:wght@700&display=swap">
<style>
  :root {
    --backdrop: #e9e5df;
    --sign-white: #ffffff;
    --brand-yellow: #fdec24;
    --brand-red: #e31b23;
    --ink: #111111;
    --base-grey: #4a4a4a;
    --sky: #e3e8e0;
    --facade: #cdbfa5;
    --lawn: #8c8a52;
  }
  html, body {
    margin: 0;
    width: 1200px;
    height: 1200px;
    overflow: hidden;
    background: var(--backdrop);
  }
  .sign {
    position: absolute;
    left: 320px;
    top: 40px;
    width: 560px;
    height: 1120px;
    box-shadow: 0 10px 30px rgba(0,0,0,0.25);
  }
  .sign svg { display: block; width: 100%; height: 100%; }
  .brand-name {
    font-family: "Oswald", sans-serif;
    font-weight: 700;
    fill: var(--brand-red);
  }
  .opening-line {
    font-family: "Open Sans", sans-serif;
    font-weight: 400;
    font-size: 50px;
    fill: var(--brand-red);
    letter-spacing: 1px;
  }
  .tagline {
    font-family: "Open Sans", sans-serif;
    fill: var(--ink);
  }
  .tagline-light { font-weight: 400; font-size: 36px; }
  .tagline-bold { font-weight: 700; font-size: 48px; }
  .tagline-large { font-weight: 400; font-size: 66px; letter-spacing: -2px; }
  .web-address {
    font-family: "Open Sans", sans-serif;
    font-weight: 700;
    font-size: 22px;
    fill: var(--brand-red);
  }
</style>
</head>
<body>
  <div class="sign">
    <svg viewBox="0 0 550 1100" xmlns="http://www.w3.org/2000/svg">
      <defs>
        <linearGradient id="rendering-tone" x1="0" y1="0" x2="0" y2="1">
          <stop offset="0" stop-color="var(--sky)"/>
          <stop offset="0.45" stop-color="var(--sky)"/>
          <stop offset="0.55" stop-color="var(--facade)"/>
          <stop offset="0.78" stop-color="var(--facade)"/>
          <stop offset="0.86" stop-color="var(--lawn)"/>
          <stop offset="1" stop-color="var(--lawn)"/>
        </linearGradient>
        <linearGradient id="base-shade" x1="0" y1="0" x2="0" y2="1">
          <stop offset="0" stop-color="#2e2e2e"/>
          <stop offset="1" stop-color="#6a6a6a"/>
        </linearGradient>
      </defs>

      <rect class="sign-field" width="550" height="1100" fill="var(--sign-white)"/>
      <polygon class="corner-wedge" points="410,0 550,0 550,253" fill="var(--brand-yellow)"/>

      <g class="brand-lockup">
        <text class="brand-name" x="275" y="110" text-anchor="middle" font-size="64">Harbor</text>
        <text class="brand-name" x="275" y="195" text-anchor="middle" font-size="64">Locker</text>
        <text class="brand-name" x="275" y="280" text-anchor="middle" font-size="64">Yard</text>
      </g>

      <polygon class="diagonal-yellow" points="0,540 267,438 550,255 550,290 0,880" fill="var(--brand-yellow)"/>
      <polygon class="diagonal-red" points="0,793 550,255 550,266 0,838" fill="var(--brand-red)"/>

      <polygon class="facility-rendering" role="img"
               aria-label="Architectural rendering of the storage facility building with trees and lawn"
               points="0,872 550,272 550,1030 0,1030" fill="url(#rendering-tone)"/>

      <text class="opening-line" transform="translate(34,722) rotate(-44.4)">OPENING FALL 2016</text>

      <g class="tagline" text-anchor="end">
        <text class="tagline tagline-light" x="515" y="786">Your</text>
        <text class="tagline tagline-bold" x="515" y="846">Premier</text>
        <text class="tagline tagline-large" x="515" y="923">SELF-STORAGE</text>
        <text class="tagline tagline-large" x="515" y="998">FACILITY</text>
      </g>

      <rect class="address-band" x="0" y="1030" width="550" height="44" fill="var(--sign-white)"/>
      <text class="web-address" x="275" y="1059" text-anchor="middle">www.harborlockeryard.example</text>
      <rect class="sign-base" x="0" y="1074" width="550" height="26" fill="url(#base-shade)"/>
    </svg>
  </div>
</body>
</html>
```